Banner Ad Design for Resume Builder Needed

For the ad copy and design of the ad, I leave that up to you. Keep in mind this is a do-it-yourself online resume builder. The site is simple to use and geared towards people who are unsure of how to write/create their own resume.

You can view the site (which isn't finished) and how it works at http://careerforge.demo.tlvworks.net/

I do not want the same color scheme or the logo used in the ad, just the most appealing ad for those looking to use a product like this

I need the ad in these sizes:

300x250, 728x90, 160x600, 468x60, 120x600, 300x100

```html
<!DOCTYPE html>
<html lang="en">
<head>
<meta charset="utf-8">
<title>CvAscend — Banner Set</title>
<link rel="stylesheet" href="https://fonts.googleapis.com/css2?family=Arimo:ital,wght@0,400;0,700;1,700&display=swap">
<style>
  :root {
    --page: #ffffff;
    --ink: #141414;
    --label: #333333;
    --white: #ffffff;
    --cyan: #22c4dc;
    --slate-dark: #262d31;
    --slate-light: #4d575d;
    --desk: #d9772f;
    --desk-light: #e58a43;
    --edge-blue: #2a8fe0;
    --silver: #c9cdd0;
    --btn-top: #fbb02a;
    --btn-bottom: #e57600;
    --btn-rim: #ffd88a;
    --accent-square: #f39318;
    --frame: #9aa0a4;
  }
  * { box-sizing: border-box; margin: 0; padding: 0; }
  html, body { width: 1200px; height: 1200px; overflow: hidden; background: var(--page); }
  body { position: relative; font-family: "Arimo", Arial, sans-serif; color: var(--ink); }

  .banner { position: absolute; overflow: hidden; border: 1px solid var(--frame); background: var(--cyan); }
  .banner svg.layer { position: absolute; inset: 0; width: 100%; height: 100%; }

  .size-label { position: absolute; font-size: 20px; color: var(--label); transform: translateX(-50%); letter-spacing: 0.5px; }

  .headline { position: absolute; font-weight: 700; text-align: center; line-height: 1.08; color: var(--ink); }
  .product { position: absolute; font-weight: 700; font-style: italic; color: var(--white); line-height: 1.05; white-space: nowrap; text-shadow: 0 1px 2px rgba(0,0,0,.4); }
  .byline { position: absolute; color: var(--white); font-size: 16px; white-space: nowrap; }

  .brand { position: absolute; display: flex; align-items: center; gap: 8px; color: var(--white); font-weight: 400; }
  .brand-mark { background: var(--accent-square); flex: none; }

  .cta {
    position: absolute; display: flex; align-items: center; justify-content: center; gap: 10px;
    border-radius: 999px; border: 2px solid var(--btn-rim);
    background: linear-gradient(var(--btn-top), var(--btn-bottom));
    color: var(--white); font-weight: 700; text-align: center; line-height: 1.05;
    box-shadow: 0 2px 4px rgba(0,0,0,.3);
  }
  .cta-arrow { flex: none; }

  /* 728 x 90 */
  .leaderboard { left: 134px; top: 123px; width: 928px; height: 113px; }
  .leaderboard .headline { left: 0; top: 10px; width: 205px; font-size: 25px; }
  .leaderboard .product { left: 218px; top: 14px; width: 220px; font-size: 22px; line-height: 27px; text-align: center; }
  .leaderboard .byline { left: 218px; top: 70px; width: 220px; text-align: center; }
  .leaderboard .brand { left: 702px; top: 14px; font-size: 29px; }
  .leaderboard .brand-mark { width: 24px; height: 24px; }
  .leaderboard .cta { left: 715px; top: 60px; width: 191px; height: 40px; font-size: 14px; }

  /* 300 x 250 */
  .rectangle { left: 134px; top: 327px; width: 383px; height: 319px; }
  .rectangle .headline { left: 0; top: 16px; width: 383px; font-size: 26px; }
  .rectangle .product { left: 22px; top: 86px; font-size: 23px; }
  .rectangle .byline { right: 38px; top: 117px; }
  .rectangle .brand { left: 210px; top: 196px; font-size: 26px; }
  .rectangle .brand-mark { width: 22px; height: 22px; }
  .rectangle .cta { left: 188px; top: 258px; width: 189px; height: 41px; font-size: 14px; }

  /* 160 x 600 */
  .skyscraper { left: 845px; top: 328px; width: 204px; height: 766px; }
  .skyscraper .headline { left: 0; top: 12px; width: 204px; font-size: 27px; }
  .skyscraper .product { left: 0; top: 152px; width: 204px; text-align: center; font-size: 39px; }
  .skyscraper .byline { left: 0; top: 274px; width: 204px; text-align: center; }
  .skyscraper .brand { left: 22px; top: 610px; font-size: 25px; }
  .skyscraper .brand-mark { width: 22px; height: 22px; }
  .skyscraper .cta { left: 13px; top: 664px; width: 181px; height: 86px; font-size: 22px; }
</style>
</head>
<body>

<!-- 728 x 90 -->
<section class="banner leaderboard">
  <svg class="layer" viewBox="0 0 928 113" preserveAspectRatio="none" aria-hidden="true">
    <defs>
      <linearGradient id="slateA" x1="0" y1="0" x2="0" y2="1">
        <stop offset="0" stop-color="var(--slate-light)"/><stop offset="1" stop-color="var(--slate-dark)"/>
      </linearGradient>
      <linearGradient id="paperA" x1="0" y1="0" x2="1" y2="0">
        <stop offset="0" stop-color="#ffffff"/><stop offset="1" stop-color="#dcdcdc"/>
      </linearGradient>
    </defs>
    <rect width="928" height="113" fill="var(--cyan)"/>
    <polygon points="200,0 460,0 410,113 200,113" fill="url(#slateA)"/>
    <path d="M0 0 H205 Q226 56 205 113 H0 Z" fill="url(#paperA)"/>
    <path d="M206 0 Q227 56 206 113" fill="none" stroke="var(--edge-blue)" stroke-width="6"/>
  </svg>
  <svg class="layer" viewBox="0 0 928 113" preserveAspectRatio="none" role="img" aria-label="Illustration of a desk with a hand writing a CV, glasses, pens and coffee">
    <defs>
      <linearGradient id="deskA" x1="0" y1="0" x2="1" y2="1">
        <stop offset="0" stop-color="var(--desk-light)"/><stop offset="1" stop-color="var(--desk)"/>
      </linearGradient>
    </defs>
    <polygon points="457,0 621,0 704,113 408,113" fill="url(#deskA)"/>
  </svg>
  <svg class="layer" viewBox="0 0 928 113" preserveAspectRatio="none" aria-hidden="true">
    <polygon points="619,0 636,0 719,113 702,113" fill="var(--silver)"/>
  </svg>

  <h2 class="headline">NO<br>WRITING<br>EXPERIENCE</h2>
  <p class="product">ONLINE RESUME<br>BUILDER</p>
  <p class="byline">by Do It YourSelf</p>
  <div class="brand"><span class="brand-mark"></span>CvAscend</div>
  <div class="cta">BUILD THE RESUME
    <svg class="cta-arrow" width="24" height="24" viewBox="0 0 24 24" aria-hidden="true">
      <circle cx="12" cy="12" r="11" fill="#fff"/>
      <path d="M6 10.5h6v-4l6 5.5-6 5.5v-4H6z" fill="var(--btn-bottom)"/>
    </svg>
  </div>
</section>
<span class="size-label" style="left:597px; top:243px;">728X90</span>

<!-- 300 x 250 -->
<section class="banner rectangle">
  <svg class="layer" viewBox="0 0 383 319" preserveAspectRatio="none" aria-hidden="true">
    <defs>
      <linearGradient id="slateB" x1="0" y1="0" x2="0" y2="1">
        <stop offset="0" stop-color="var(--slate-light)"/><stop offset="1" stop-color="var(--slate-dark)"/>
      </linearGradient>
      <linearGradient id="paperB" x1="0" y1="0" x2="0" y2="1">
        <stop offset="0" stop-color="#ffffff"/><stop offset="1" stop-color="#d8d8d8"/>
      </linearGradient>
    </defs>
    <rect width="383" height="319" fill="var(--cyan)"/>
    <polygon points="0,55 383,55 383,158 0,133" fill="url(#slateB)"/>
    <path d="M0 0 H383 V60 Q191 38 0 60 Z" fill="url(#paperB)"/>
    <path d="M0 60 Q191 38 383 60" fill="none" stroke="var(--edge-blue)" stroke-width="6"/>
  </svg>
  <svg class="layer" viewBox="0 0 383 319" preserveAspectRatio="none" role="img" aria-label="Illustration of a desk with a hand writing a CV, glasses, pens and coffee">
    <defs>
      <linearGradient id="deskB" x1="0" y1="0" x2="1" y2="1">
        <stop offset="0" stop-color="var(--desk-light)"/><stop offset="1" stop-color="var(--desk)"/>
      </linearGradient>
    </defs>
    <polygon points="0,133 245,151 168,319 0,319" fill="url(#deskB)"/>
  </svg>
  <svg class="layer" viewBox="0 0 383 319" preserveAspectRatio="none" aria-hidden="true">
    <polygon points="245,151 263,152 186,319 168,319" fill="var(--silver)"/>
  </svg>

  <h2 class="headline">NO WRITING EXPERIENCE</h2>
  <p class="product">ONLINE RESUME BUILDER</p>
  <p class="byline">by Do It YourSelf</p>
  <div class="brand"><span class="brand-mark"></span>CvAscend</div>
  <div class="cta">BUILD THE RESUME
    <svg class="cta-arrow" width="24" height="24" viewBox="0 0 24 24" aria-hidden="true">
      <circle cx="12" cy="12" r="11" fill="#fff"/>
      <path d="M6 10.5h6v-4l6 5.5-6 5.5v-4H6z" fill="var(--btn-bottom)"/>
    </svg>
  </div>
</section>
<span class="size-label" style="left:323px; top:653px;">300X250</span>

<!-- 160 x 600 -->
<section class="banner skyscraper">
  <svg class="layer" viewBox="0 0 204 766" preserveAspectRatio="none" aria-hidden="true">
    <defs>
      <linearGradient id="slateC" x1="0" y1="0" x2="0" y2="1">
        <stop offset="0" stop-color="var(--slate-light)"/><stop offset="1" stop-color="var(--slate-dark)"/>
      </linearGradient>
      <linearGradient id="paperC" x1="0" y1="0" x2="0" y2="1">
        <stop offset="0" stop-color="#ffffff"/><stop offset="1" stop-color="#d6d6d6"/>
      </linearGradient>
    </defs>
    <rect width="204" height="766" fill="var(--cyan)"/>
    <polygon points="0,116 204,116 204,375 0,318" fill="url(#slateC)"/>
    <path d="M0 0 H204 V122 Q102 100 0 122 Z" fill="url(#paperC)"/>
    <path d="M0 122 Q102 100 204 122" fill="none" stroke="var(--edge-blue)" stroke-width="6"/>
  </svg>
  <svg class="layer" viewBox="0 0 204 766" preserveAspectRatio="none" role="img" aria-label="Illustration of a desk with a hand writing a CV, glasses, pens and coffee">
    <defs>
      <linearGradient id="deskC" x1="0" y1="0" x2="1" y2="1">
        <stop offset="0" stop-color="var(--desk-light)"/><stop offset="1" stop-color="var(--desk)"/>
      </linearGradient>
    </defs>
    <polygon points="0,318 204,375 204,382 0,605" fill="url(#deskC)"/>
  </svg>
  <svg class="layer" viewBox="0 0 204 766" preserveAspectRatio="none" aria-hidden="true">
    <polygon points="204,380 204,400 0,627 0,605" fill="var(--silver)"/>
  </svg>

  <h2 class="headline">NO<br>WRITING<br>EXPERIENCE</h2>
  <p class="product">ONLINE<br>RESUME<br>BUILDER</p>
  <p class="byline">by Do It YourSelf</p>
  <div class="brand"><span class="brand-mark"></span>CvAscend</div>
  <div class="cta">BUILD YOUR<br>RESUME</div>
</section>
<span class="size-label" style="left:942px; top:1100px;">160X600</span>

</body>
</html>
```